Letterhead and email signiture

Hello,

I have an example of a letterhead that we need. The one we have constandly moves if we paste any information in it. We are looking for one that is permanent. We only need the top of the letterhead on the first page but the bottom on each and every page afterward.

It does not have to be exactly what I am providing here. Please take a look at the website and maybe you will have a better idea.

We are looking to do something similar for an email signature

Marvistoinc.com

```html
<!DOCTYPE html>
<html lang="en">
<head>
<meta charset="utf-8">
<title>Marvisto Inc — Letterhead and Email Signature</title>
<link href="https://fonts.googleapis.com/css2?family=Arimo:wght@400;700&display=swap" rel="stylesheet">
<style>
  :root {
    --backdrop: #3b3b3d;
    --paper: #f4f2f2;
    --ink: #111111;
    --text: #444444;
    --muted: #555555;
    --accent-black: #000000;
    --icon-blue: #3a7fd0;
  }
  * { margin: 0; padding: 0; box-sizing: border-box; }
  html, body { width: 1200px; height: 826px; overflow: hidden; }
  body {
    background: var(--backdrop);
    font-family: "Arimo", Arial, sans-serif;
    position: relative;
  }

  /* Letterhead sheet */
  .letterhead {
    position: absolute;
    left: 67px; top: 72px;
    width: 496px; height: 698px;
    background: var(--paper);
    box-shadow: 0 2px 8px rgba(0,0,0,0.35);
    overflow: hidden;
  }
  .corner-swoosh { position: absolute; top: 0; right: 0; }
  .brand-name {
    font-family: "Arimo", Arial, sans-serif;
    font-weight: 700;
    color: var(--ink);
    letter-spacing: -0.5px;
    white-space: nowrap;
  }
  .letterhead .brand-name {
    position: absolute;
    left: 0; width: 494px; top: 50px;
    text-align: center;
    font-size: 19px;
  }
  .salutation {
    position: absolute; left: 49px; top: 170px;
    font-size: 13.5px; color: var(--text);
  }
  .letter-body {
    position: absolute; left: 49px; top: 211px; width: 399px;
    font-size: 7.4px; line-height: 11.9px; color: var(--muted);
    text-align: justify;
  }
  .letter-body p { margin-bottom: 11.9px; }
  .closing {
    position: absolute; left: 49px; top: 473px;
    font-size: 7.6px; color: var(--muted);
  }
  .signature-mark {
    position: absolute; left: 47px; top: 492px;
    width: 64px; height: 26px;
    background: linear-gradient(90deg, rgba(30,40,60,0.18), rgba(30,40,60,0.05));
    border-radius: 3px;
  }
  .signer-name {
    position: absolute; left: 51px; top: 530px;
    font-size: 11.5px; color: var(--text);
  }
  .signer-title {
    position: absolute; left: 51px; top: 546px;
    font-size: 8.4px; color: var(--muted);
  }
  .letter-footer {
    position: absolute; left: 0; width: 496px; top: 662px;
    text-align: center;
    font-size: 7.8px; line-height: 12.6px; color: var(--ink);
  }

  /* Email signature */
  .email-signature {
    position: absolute;
    left: 626px; top: 325px;
    width: 504px; height: 139px;
    background: var(--paper);
    box-shadow: 0 2px 8px rgba(0,0,0,0.35);
    overflow: hidden;
  }
  .email-signature .brand-name {
    position: absolute; left: 33px; top: 27px;
    font-size: 25px;
  }
  .contact-list {
    position: absolute; left: 38px; top: 74px;
    list-style: none;
    font-size: 10px; line-height: 12.6px; color: var(--ink);
  }
  .contact-list li { display: flex; align-items: center; gap: 8px; }
  .contact-list svg { width: 8px; height: 8px; flex: none; }
</style>
</head>
<body>

<section class="letterhead" aria-label="Letterhead">
  <svg class="corner-swoosh" width="496" height="210" viewBox="0 0 496 210">
    <path d="M306 0 H496 V206 C470 90 400 10 306 0 Z" fill="var(--accent-black)"/>
  </svg>

  <div class="brand-name">MARVISTO INC</div>

  <p class="salutation">Dear Mr. Hart,</p>

  <div class="letter-body">
    <p>Lorem ipsum dolor sit amet, consectetur adipiscing elit. Donec orci purus, luctus vitae dignissim eu, iaculis sed purus. Vivamus faucibus, ipsum nec aliquet viverra, leo mauris condimentum ligula, sit amet sagittis enim ligula quis arcu. Nam egestas tortor id nisi porttitor mattis. In tortor ante, ultricies in suscipit a, tempus non massa. Vivamus et auctor mi. Fusce vel massa nulla. Phasellus nec eros mauris, et scelerisque orci.</p>
    <p>Donec malesuada orci vitae nulla accumsan porta a id massa. Quisque accumsan iaculis magna sit amet fringilla. Maecenas consequat, magna eget tincidunt semper, odio nibh rutrum mi, id feugiat ante nisi eu risus. Vestibulum nunc orci, rhoncus a placerat in, ultricies in mi. Cras mattis varius eros, vel fringilla nisi suscipit eget. Quisque scelerisque sagittis nulla at porttitor.</p>
    <p>Sed id augue vitae urna euismod commodo aliquet a quam. Pellentesque arcu velit, cursus et malesuada ut, consequat et diam. Nullam erat sem, rhoncus id ullamcorper vitae, rhoncus et arcu. In ultricies ultricies nulla, ut rutrum nisi iaculis at. Donec eu magna a metus ornare faucibus. Fusce aliquet faucibus ultricies. Morbi semper, est id tincidunt gravida, sem arcu adipiscing lacus, ac bibendum nulla leo eu purus. Quisque nec diam sed risus consectetur a ccumsan quis quis nibh. Vestibulum id purus lorem.</p>
    <p>It is a long established fact that a reader will be distracted by the readable content of a page when looking at its layout. The point of using Lorem Ipsum is that it has a more-or-less normal distribution of letters, as opposed to using 'Content here, content here', making it look like readable English. Many desktop publishing packages</p>
  </div>

  <p class="closing">Sincerely,</p>
  <div class="signature-mark" role="img" aria-label="Handwritten signature"></div>
  <p class="signer-name">Alan Hart</p>
  <p class="signer-title">CEO/ Founder</p>

  <footer class="letter-footer">
    This document is confidential and intended solely for investigative purposes by Marvisto Inc.<br>
    555-803-0100 &nbsp;|&nbsp; 555-530-0100 | MARVISTOINC.COM
  </footer>
</section>

<section class="email-signature" aria-label="Email signature">
  <svg class="corner-swoosh" width="504" height="139" viewBox="0 0 504 139">
    <path d="M385 0 H504 V139 C480 60 440 8 385 0 Z" fill="var(--accent-black)"/>
  </svg>

  <div class="brand-name">MARVISTO INC</div>

  <ul class="contact-list">
    <li>
      <svg viewBox="0 0 10 10" aria-hidden="true"><path d="M2 1 L4 3 L3 4 Q4 6 6 7 L7 6 L9 8 L8 9 Q3 9 1 2 Z" fill="var(--icon-blue)"/></svg>
      555-803-0100
    </li>
    <li>
      <svg viewBox="0 0 10 10" aria-hidden="true"><rect x="0.5" y="2" width="9" height="6" fill="var(--icon-blue)"/><path d="M0.5 2 L5 5.5 L9.5 2" stroke="#fff" stroke-width="0.8" fill="none"/></svg>
      555-530-0100
    </li>
    <li>
      <svg viewBox="0 0 10 10" aria-hidden="true"><circle cx="5" cy="5" r="4.5" fill="var(--icon-blue)"/><path d="M0.5 5 H9.5 M5 0.5 V9.5" stroke="#fff" stroke-width="0.6"/></svg>
      www.marvistoinc.com
    </li>
  </ul>
</section>

</body>
</html>
```